New Plumbing Company

We are looking for a smart and creative business card design for our new plumbing company. We are looking for creativity and originality in our business cards.

Industry/Entity Type

Plumbing

Contact Information for Business Card

Kelvora Plumbing
Peter Oswalt
Managing Director
Telephone Number : 0481529046
Email : service@kelvoraplumbing.com.au
Website : www.kelvoraplumbing.com.au
Lic. 318462D

Colors
0692cd
33a6d7
000000

Requirements
Must have
• I want the business card to be designed on a black background using the blue tones i have selected as seen in the company logo.

```html
<!DOCTYPE html>
<html lang="en">
<head>
<meta charset="utf-8">
<title>Kelvora Plumbing – Business Card</title>
<link href="https://fonts.googleapis.com/css2?family=Open+Sans:wght@300;400;600;700&display=swap" rel="stylesheet">
<style>
  :root {
    --stage: #2a2621;
    --card-black: #050607;
    --card-sheen: #1c1f22;
    --blue-deep: #0692cd;
    --blue-light: #33a6d7;
    --text-white: #f2f4f5;
  }
  * { box-sizing: border-box; margin: 0; padding: 0; }
  html, body {
    width: 1200px; height: 1023px; overflow: hidden;
    background: var(--stage);
    font-family: "Open Sans", Arial, sans-serif;
  }
  .stage {
    width: 1200px; height: 1023px;
    display: flex; align-items: center; justify-content: center;
  }
  .card {
    position: relative;
    width: 860px; height: 490px;
    border-radius: 34px;
    overflow: hidden;
    background: linear-gradient(125deg, var(--card-sheen) 0%, var(--card-black) 45%, var(--card-black) 100%);
    box-shadow: 0 18px 40px rgba(0,0,0,.5);
  }
  .license {
    position: absolute; top: 30px; right: 48px;
    color: var(--text-white); font-size: 19px; font-weight: 400; letter-spacing: .5px;
  }
  .brand {
    position: absolute; top: 92px; left: 56px;
    display: flex; align-items: center; gap: 22px;
  }
  .brand-dot {
    width: 74px; height: 74px; border-radius: 50%;
    background: var(--blue-deep);
  }
  .brand-name {
    color: var(--text-white); font-size: 50px; font-weight: 300; letter-spacing: .5px;
  }
  .rule {
    position: absolute; top: 194px; left: 380px; right: 0;
    height: 2px; background: var(--blue-deep);
  }
  .person { position: absolute; top: 206px; left: 120px; }
  .person-name {
    color: var(--blue-light); font-size: 27px; font-weight: 700; letter-spacing: .5px;
    text-transform: uppercase; line-height: 36px;
  }
  .person-title { color: var(--text-white); font-size: 19px; line-height: 26px; }
  .contacts { list-style: none; margin-top: 14px; }
  .contacts li {
    display: flex; align-items: center; gap: 12px;
    color: var(--text-white); font-size: 19px; line-height: 30px;
  }
  .contacts svg { width: 18px; height: 18px; flex: none; }
  .address-band {
    position: absolute; left: 0; right: 0; bottom: 0; height: 84px;
    background: linear-gradient(180deg, var(--blue-light), var(--blue-deep));
    display: flex; align-items: center; padding-left: 120px;
    color: var(--card-black); font-size: 21px; font-weight: 700; letter-spacing: .5px;
    text-transform: uppercase;
  }
  .corner-dot {
    position: absolute; right: 56px; bottom: 112px;
    width: 78px; height: 78px; border-radius: 50%;
    border: 4px solid var(--blue-deep);
  }
</style>
</head>
<body>
<main class="stage">
  <article class="card">
    <p class="license">Lic. 318462D</p>

    <div class="brand">
      <span class="brand-dot"></span>
      <span class="brand-name">Kelvora Plumbing</span>
    </div>
    <div class="rule"></div>

    <section class="person">
      <h1 class="person-name">Peter Oswalt</h1>
      <p class="person-title">Managing Director</p>
      <ul class="contacts">
        <li>
          <svg viewBox="0 0 18 18"><circle cx="9" cy="9" r="9" fill="#33a6d7"/><path d="M6 4.5l2 2-1 1.3c.6 1.3 1.5 2.2 2.8 2.8l1.3-1 2 2-1.2 1.4C9.5 12.7 5.3 8.5 4.6 5.7z" fill="#050607"/></svg>
          0481529046
        </li>
        <li>
          <svg viewBox="0 0 18 18"><circle cx="9" cy="9" r="9" fill="#33a6d7"/><rect x="4.5" y="6" width="9" height="6.5" fill="#050607"/><path d="M4.5 6l4.5 3.8L13.5 6" stroke="#33a6d7" stroke-width="1" fill="none"/></svg>
          service@kelvoraplumbing.com.au
        </li>
        <li>
          <svg viewBox="0 0 18 18"><circle cx="9" cy="9" r="9" fill="#33a6d7"/><circle cx="9" cy="9" r="4.8" fill="none" stroke="#050607" stroke-width="1.2"/><path d="M4.2 9h9.6M9 4.2v9.6" stroke="#050607" stroke-width="1.1"/></svg>
          www.kelvoraplumbing.com.au
        </li>
      </ul>
    </section>

    <span class="corner-dot"></span>

    <footer class="address-band">2250 Harbour Lane, Eastvale, Northmere</footer>
  </article>
</main>
</body>
</html>
```